Zielgruppe
Die Kessler-Volkshochschule Kreis Aurental ist eine gemeinnützige Einrichtung zur Erwachsenen- und Weiterbildung mit ca. 5.000 Veranstaltungen pro Jahr.
Volkshochschulen sind entgegen ihrer Bezeichnung keine Hochschulen oder Schulen, sondern in Deutschland dem Bildungsbereich der Weiterbildung zugeordnet.
Aufgabenstellung
Die Kessler-Volkshochschule Kreis Aurental möchte mit einer neuen Webseite, welche auch für mobile Geräte geeignet sein muss, Ihren neuen Internetauftritt umsetzen.
Vorgaben:
- der Internetauftritt soll modern gestaltet sein.
- die unter Dateien befindlichen Guidelines müssen eingehalten werden. Wichtig hierbei ist, dass die 6 Symbole auf die Startseite für die Auswahl der jeweiligen Kursbereiche integriert werden. Hierbei ist zu beachten, dass die Anzahl der Symbole erweiterbar ist.
Als CMS wird Typo3 genutzt.
Es geht um die Erstellung der Startseite auf welcher auch News untergebracht werden sollen - ggf. in Kachelform. Und die Erstellung einer Unterseite.

```html
<!DOCTYPE html>
<html lang="de">
<head>
<meta charset="utf-8">
<title>Kessler-Volkshochschule Kreis Aurental</title>
<link href="https://fonts.googleapis.com/css2?family=Arimo:wght@400;700&display=swap" rel="stylesheet">
<style>
:root{
  --navy:#0b2a5f;
  --navy-active:#3a5a88;
  --footer-band:#3b5784;
  --footer-base:#08265c;
  --orange:#e8620f;
  --ink:#222;
  --muted:#555;
  --tile:#e8e8e8;
  --white:#fff;
  --blue:#5bb4e5;--purple:#8456a6;--green:#a6c312;--red:#e3000f;--orange2:#ef6a10;--yellow:#f6b800;
}
*{box-sizing:border-box;margin:0;padding:0}
html,body{width:853px;height:1200px;overflow:hidden;background:var(--white);font-family:"Arimo",Arial,sans-serif;color:var(--ink)}
.page{position:relative;width:853px;height:1200px}
.abs{position:absolute}
.brand{left:80px;top:34px;display:flex;align-items:center;gap:8px}
.brand-dot{width:14px;height:14px;border-radius:50%;background:var(--navy)}
.brand-name{font-size:13px;line-height:15px;color:var(--navy);border-left:1px solid #bbb;padding-left:8px}
.brand-name span{display:block}
.top-links{right:80px;top:53px;display:flex;gap:18px;font-size:10.5px;color:var(--ink)}
.main-nav{left:80px;top:82px;width:693px;height:29px;display:flex;background:var(--navy)}
.main-nav a{flex:1;color:var(--white);text-decoration:none;font-size:10.5px;display:flex;align-items:center;justify-content:center;border-right:1px solid #fff}
.main-nav a:last-child{border-right:0}
.main-nav a.active{background:var(--navy-active)}
.hero{left:80px;top:111px;width:693px;height:313px;background:linear-gradient(100deg,#e9e3dc 0%,#c9b7a4 30%,#6e5a4c 55%,#efeae6 80%,#f6f4f2 100%)}
.hero-title{left:119px;top:265px;background:rgba(255,255,255,.85);padding:4px 12px 6px 11px}
.hero-title h1{font-size:22px;line-height:24px;font-weight:700}
.hero-title p{font-size:17px;font-weight:700;line-height:20px}
.btn{background:var(--orange);color:var(--white);font-weight:700;font-size:10.5px;display:flex;align-items:center;justify-content:center;text-decoration:none}
.hero-btn{left:130px;top:333px;width:131px;height:33px}
.login{left:476px;top:169px;width:263px;height:197px;background:rgba(255,255,255,.95);border-radius:6px;padding:19px 34px}
.login h2{font-size:16px;font-weight:700;margin-bottom:8px}
.field{width:193px;height:33px;border:1px solid var(--navy);font-size:11px;color:#777;padding:0 12px;display:flex;align-items:center;margin-bottom:13px;font-weight:700}
.login-foot{display:flex;justify-content:space-between;align-items:flex-start}
.login-links a{display:block;font-size:7px;color:var(--ink);line-height:12.5px}
.login-btn{width:62px;height:33px;margin-top:-1px}
.section-title{font-size:16.5px;font-weight:700;left:79px}
.courses{left:80px;top:486px;display:flex;gap:19px}
.course{width:100px;text-align:center}
.course-tile{width:100px;height:100px;background:var(--tile);display:flex;align-items:center;justify-content:center}
.course-tile span{width:80px;height:80px;border-radius:50%;border:2px solid #fff}
.course p{font-size:11px;font-weight:700;margin-top:6px}
.news{left:80px;top:663px;width:693px;height:187px;background:var(--tile)}
.news-arrow{position:absolute;top:83px;font-size:20px;color:#fff;font-weight:700}
.news-cards{position:absolute;left:28px;top:19px;display:flex;gap:19px}
.news-card{width:200px;height:150px;background:var(--white);padding:15px 18px}
.news-card h3{font-size:15.5px;font-weight:700;margin-bottom:8px}
.news-card h4{font-size:11px;font-weight:700;line-height:15px}
.news-card p{font-size:11px;line-height:15px;color:var(--muted);height:15px}
.news-card .btn{width:92px;height:33px;margin-top:14px}
.promos{left:80px;top:882px;display:flex;gap:19px}
.promo{position:relative;width:218px;height:187px}
.promo-text{position:absolute;left:19px;top:106px;color:var(--white);font-size:11px;font-weight:700;line-height:12.5px}
.promo-text.dark{color:var(--ink)}
.promo .btn{position:absolute;left:19px;top:138px;width:92px;height:33px}
.footer-links{left:0;top:1100px;width:853px;height:65px;background:var(--footer-band);padding-top:15px}
.footer-links div{display:flex;justify-content:center;gap:13px;margin-bottom:8px}
.footer-links a{color:var(--white);font-size:9px;text-decoration:underline}
.copyright{left:0;top:1165px;width:853px;height:35px;background:var(--footer-base);color:var(--white);font-size:9px;padding:11px 80px}
</style>
</head>
<body>
<div class="page">
  <div class="abs brand"><span class="brand-dot"></span><div class="brand-name"><span>Kessler-Volkshochschule</span><span>Landkreis Aurental</span></div></div>
  <nav class="abs top-links"><span>Öffnungszeiten</span><span>Kontakt</span><span>Impressum</span></nav>
  <nav class="abs main-nav">
    <a class="active">Startseite</a><a>Kursprogramm</a><a>Förderungen</a><a>Service</a><a>Unterrichtsstätten</a><a>Stellenbörse</a>
  </nav>
  <div class="abs hero" role="img" aria-label="Foto: vier junge Erwachsene arbeiten gemeinsam an einem Laptop"></div>
  <div class="abs hero-title"><h1>Kessler-Volkshochschule</h1><p>Über 5.000 Veranstaltungen</p></div>
  <a class="abs btn hero-btn">Jetzt Kurse entdecken</a>
  <form class="abs login">
    <h2>Teilnehmer-Portal</h2>
    <div class="field">Teilnehmer Nr.</div>
    <div class="field">Passwort</div>
    <div class="login-foot">
      <div class="login-links"><a>Teilnehmer Nummer vergessen?</a><a>Passwort vergessen?</a><a>Erstregistrierung</a></div>
      <span class="btn login-btn">Login</span>
    </div>
  </form>
  <h2 class="abs section-title" style="top:452px">Unser Kursangebot</h2>
  <div class="abs courses">
    <div class="course"><div class="course-tile"><span role="img" aria-label="Symbol Beruf" style="background:var(--blue)"></span></div><p>Beruf</p></div>
    <div class="course"><div class="course-tile"><span role="img" aria-label="Symbol Sprachen" style="background:var(--purple)"></span></div><p>Sprachen</p></div>
    <div class="course"><div class="course-tile"><span role="img" aria-label="Symbol Gesundheit" style="background:var(--green)"></span></div><p>Gesundheit</p></div>
    <div class="course"><div class="course-tile"><span role="img" aria-label="Symbol Kultur" style="background:var(--red)"></span></div><p>Kultur</p></div>
    <div class="course"><div class="course-tile"><span role="img" aria-label="Symbol Gesellschaft" style="background:var(--orange2)"></span></div><p>Gesellschaft</p></div>
    <div class="course"><div class="course-tile"><span role="img" aria-label="Symbol Grundbildung" style="background:var(--yellow)"></span></div><p>Grundbildung</p></div>
  </div>
  <h2 class="abs section-title" style="top:629px">VHS-News</h2>
  <section class="abs news">
    <span class="news-arrow" style="left:8px">‹</span>
    <div class="news-cards">
      <article class="news-card"><h3>Medien/Film</h3><h4>Wir drehen einen Knettrickfilm - für Kinder ab 8 Jahren</h4><p>Lindenau am Talbach</p><a class="btn">Mehr erfahren</a></article>
      <article class="news-card"><h3>Führung</h3><h4>Führung im Tierpark Auenhain – Blick hinter die Kulissen</h4><p>Steinfeld</p><a class="btn">Mehr erfahren</a></article>
      <article class="news-card"><h3>EDV</h3><h4>Satzprogramm Layoutkurs – Grundlagen</h4><p>Birkental-Weiler</p><a class="btn">Mehr erfahren</a></article>
    </div>
    <span class="news-arrow" style="right:8px">›</span>
  </section>
  <div class="abs promos">
    <div class="promo" role="img" aria-label="Foto: lächelnde Frau mit Brille und Büchern" style="background:linear-gradient(120deg,#f2f0ec,#d8d2cb 50%,#2a9fd6 80%)"><div class="promo-text dark">Kessler- Volkshochschule<br>Wir über uns</div><a class="btn">Mehr erfahren</a></div>
    <div class="promo" role="img" aria-label="Foto: lächelnde junge Frau im Kursraum" style="background:linear-gradient(110deg,#5a4030,#9a7a5c 45%,#e8c8a0 75%,#d9b9a0)"><div class="promo-text">Fortbildungen für<br>Kursleiter</div><a class="btn">Mehr erfahren</a></div>
    <div class="promo" role="img" aria-label="Gruppenfoto der Dozentinnen und Dozenten" style="background:linear-gradient(180deg,#e3d7b6,#7a5a48 50%,#2e2a2a)"><div class="promo-text">Unsere<br>Dozenten an der VHS</div><a class="btn">Mehr erfahren</a></div>
  </div>
  <footer>
    <div class="abs footer-links">
      <div><a>Kontakt</a><a>Partner</a><a>AGB</a><a>Impressum</a><a>Widerruf</a></div>
      <div><a>Kursprogramm</a><a>Öffnungszeiten</a><a>Förderungen</a><a>Service</a><a>Unterrichtsstätten</a><a>Wir über uns</a><a>Fortbildungen für Kursleiter</a><a>Unsere Dozenten</a><a>Stellenbörse</a></div>
    </div>
    <div class="abs copyright">Copyright © 2014 Kessler Volkshochschule</div>
  </footer>
</div>
</body>
</html>
```